Wordpress Design Project

Hi- We are seeking a Wordpress Theme Design that will best serve as an introduction of our company, Pellwick Trading Co, to potential international clients on the web.

We are a relationship management company that help build connections between professional music equipment manufacturers and high-volume professional music equipment users, i.e concert venue managers, equipment resellers, club owners, djs,etc.

We would like to see designs to incorporate the following:

- If possible a music theme tastefully designed into the company name/logo on the wordpress home page (not a dealbreaker without)

-We are choosing the Wordpress CMS because we're looking for the site to be more centered around our blog, which will be the main medium where we connect with clients and potential clients, where these previously strangers that we meet briefly on our travelings can get to know us better by coming to the site. The relationship, and the rapport that they feel towards my team and I, will be the key driver in determining whether they will want to do business through us or not. The products are secondary in importance. It is after the visitor feel comfortable doing business through us that they will venture to check out the products that we offer. Finally, the website is not a sales point, there will not be a feature for someone to buy something from the site.

Long story short, this website is meant to be a communications channel and not a sales channel.

-Need a contacts form application built-in to capture interested client information to facilitate the off-site sales process.

- Would prefer the theme to give a minimalist and conservative feel, and ideally capture the concept of our globalized world and the synergizing role that music plays in bringing people together.

-Ideally the design should incorporate subtle references to the Generation Y values that inspired our company name and mission:

-Emphasis on partnership and teamwork
-Belief and aspiration for win/win trade relations
-Fast, honest, and transparent service
-Make the world a better place via trade

Theme example (function-wise): http://demo2.larkpanes.com/?name=smpl

Product Type examplex: http://www.qolv.com.cn/en/product.asp

(Willing to pay extra if the winning design can be coded to full functionality)
Updates

To all those designers who've accepted the contest invitation, can you please send me a quick message to confirm if you are still planning on submitting by the end of the day tomorrow, 8/9. Otherwise we will make a selection ahead of the deadline so we can speed up our website live date. Thanks!

Target Market(s)

High volume/frequency professional music equipment users/resellers. Concert venues, DJs, Dance Clubs, etc

Industry/Entity Type

Communications

Requirements
Must have
• Blog
Product Showcase Page that is easy to update and expand.
About Page
Contact Forms Application built-in
Nice to have
• Music theme designed into company name/logo

```html
<!DOCTYPE html>
<html lang="en">
<head>
<meta charset="utf-8">
<title>Pellwick Trading Co</title>
<link href="https://fonts.googleapis.com/css2?family=Oswald:wght@400;500&family=Open+Sans:ital,wght@0,400;0,600;0,700;1,400&family=Playfair+Display:wght@700&display=swap" rel="stylesheet">
<style>
:root{
  --ink:#222;
  --text:#333;
  --muted:#888;
  --red:#c9392b;
  --dark:#2a2a2a;
  --bar:#2d2d2d;
  --page:#efefef;
  --nav:#c8c8c8;
  --nav-active:#b2b2b2;
  --rule:#dcdcdc;
  --white:#fff;
}
*{margin:0;padding:0;box-sizing:border-box}
html,body{width:720px;height:1200px;overflow:hidden;background:var(--page);font-family:"Open Sans",Arial,sans-serif;color:var(--text)}
.canvas{position:relative;width:720px;height:1200px}
.abs{position:absolute}
a{color:inherit;text-decoration:none}

/* top bar */
.topbar{left:0;top:0;width:720px;height:28px;background:var(--bar)}
.toplinks{left:84px;top:8px;font-size:8px;color:#eee;display:flex;gap:13px}
.signin{left:372px;top:9px;font-size:7.5px;font-weight:700;color:#fff}
.field{height:15px;top:7px;border-radius:8px;background:#4a4a4a;color:#999;font-size:7px;padding:3px 9px}
.go{left:568px;top:7px;width:18px;height:15px;border-radius:8px;background:var(--red);color:#fff;font-size:7px;font-weight:700;text-align:center;line-height:15px}
.divider{left:600px;top:6px;width:1px;height:16px;background:#777}
.signup{left:608px;top:9px;font-size:7.5px;color:var(--red);font-weight:600;text-decoration:underline}

/* header */
.logo-mark{left:72px;top:38px;width:36px;height:36px;border-radius:50%;background:var(--ink)}
.logo-name{left:116px;top:47px;font-family:"Oswald",sans-serif;font-weight:500;font-size:17px;color:var(--ink)}
.banner{left:361px;top:40px;width:287px;height:35px;border:2px solid var(--ink);background:#fff;padding:2px}
.banner-fill{width:100%;height:100%;background:linear-gradient(90deg,#fff 15%,#b8572a 35%,#c96a35 55%,#8a3a1c 70%,#fff 85%)}

/* nav */
.nav{left:72px;top:86px;width:576px;height:29px;background:var(--nav);display:flex}
.nav a{font-family:"Oswald",sans-serif;font-size:8px;color:var(--ink);display:flex;align-items:center;justify-content:center;border-right:1px solid #b5b5b5;height:100%}
.nav a.active{background:var(--nav-active);color:#fff}
.search{left:496px;top:94px;width:140px;height:14px;border-radius:7px;background:#fff;font-size:7px;color:#999;font-style:italic;padding:2px 11px}

/* main */
.main{left:72px;top:126px;width:576px;height:736px;background:var(--white);border-radius:5px 5px 0 0}
.hero{left:90px;top:145px;width:384px;height:188px;background:linear-gradient(90deg,#d8817a 0%,#cd6c67 45%,#b85956 100%)}
.hero-piano{left:296px;top:150px;width:170px;height:180px;background:linear-gradient(160deg,#3a3a3a,#0c0c0c 60%,#222);border-radius:60px 30px 4px 4px;opacity:.9}
.hero-kicker{left:201px;top:182px;font-family:"Playfair Display",serif;font-size:10.5px;color:#3a1d1c}
.hero-title{left:113px;top:190px;font-family:"Playfair Display",serif;font-size:27px;line-height:34px;color:#fff}
.hero-sub{left:114px;top:219px;font-size:9px;color:#3a1d1c}

.sec-title{font-family:"Oswald",sans-serif;font-size:15px;color:var(--ink)}
.sec-sub{font-size:6.5px;color:#666}
.rule{height:1px;background:var(--rule)}

.photo-guitar{width:120px;height:91px;background:radial-gradient(ellipse at 45% 60%,#e8e2d8 0%,#cfc6b8 25%,#8a1e18 45%,#1a0606 80%)}
.cap{font-size:7px;color:#222;width:130px;white-space:nowrap}
.price{font-size:7px;color:var(--red);white-space:nowrap}
.price .sep{color:#333;margin:0 4px}
.price .enquire{color:#555;display:inline-flex;align-items:center;gap:3px}

.more{left:402px;top:670px;width:66px;height:18px;background:#111;color:#fff;font-size:7.5px;font-weight:700;text-align:center;line-height:18px}

.photo-violin{width:107px;height:67px;background:radial-gradient(ellipse at 40% 55%,#e07a3a 0%,#c4501f 35%,#7a2a10 60%,#120504 90%)}
.details{color:#222;text-decoration:underline}

/* sidebar */
.photo-keys{width:135px;height:71px;background:linear-gradient(170deg,#111 0%,#333 30%,#e8e8e8 55%,#fff 75%,#bbb 100%)}
.blog-title{font-size:7.5px;color:var(--red);width:150px;white-space:nowrap}
.blog-text{font-size:7px;color:#333;width:145px;line-height:11px}
.blog-date{font-size:6.5px;color:#888}
.blog-date i{font-style:italic}
.tweet{font-size:7.5px;color:#333;line-height:10.5px}
.tweet .link{color:var(--red)}
.tweet .meta{color:#888}

/* lower band */
.redband{left:72px;top:862px;width:576px;height:5px;background:var(--red)}
.lower{left:72px;top:867px;width:576px;height:141px;background:#fff}
.about-title{left:84px;top:884px;font-family:"Oswald",sans-serif;font-size:10.5px;color:var(--ink)}
.about-title i{font-style:italic;font-weight:500}
.about-text{font-size:7px;line-height:9.3px;color:#555}
.about-box{left:232px;top:891px;width:81px;height:51px;background:#25282b}
.vline{left:328px;top:876px;width:1px;height:122px;background:#555}
.vdot{left:324px;top:933px;width:9px;height:9px;border-radius:50%;border:1px solid #555;background:#fff}
.news-title{left:342px;top:884px;font-family:"Oswald",sans-serif;font-size:10.5px;color:var(--ink)}
.news-input{left:342px;top:904px;width:168px;height:22px;border:1px solid #999;border-radius:3px;background:#fff;font-size:7.5px;font-style:italic;color:#888;padding:5px 7px}
.news-btn{left:462px;top:905px;width:47px;height:20px;background:var(--red);border-radius:2px;color:#fff;font-size:7.5px;font-style:italic;text-align:center;line-height:20px}
.follow{left:341px;top:945px;width:37px;height:39px;border:1px solid #999;border-radius:3px;background:#f6f6f6}
.follow-btn{left:344px;top:972px;width:31px;height:10px;background:var(--red);border-radius:2px;color:#fff;font-size:6.5px;font-style:italic;text-align:center;line-height:10px}
.follow-dot{left:353px;top:951px;width:13px;height:13px;background:#333;border-radius:50%}
.rt-box{left:383px;top:945px;width:253px;height:40px;border:1px solid #999;border-radius:3px;background:#fff;font-size:7.5px;font-style:italic;color:#666;padding:8px 12px;line-height:11px}
.rt-box .link{color:var(--red);font-weight:600}

/* footer */
.footer{left:72px;top:1008px;width:576px;height:149px;background:var(--dark)}
.fcol-title{font-family:"Oswald",sans-serif;font-size:10px;color:#fff}
.fcol-rule{height:1px;background:#555}
.flist{font-size:7.5px;color:#ddd;line-height:14.4px;list-style:none}
.pp-thumb{width:32px;height:32px;background:#fff}
.pp-thumb div{width:100%;height:100%;background:radial-gradient(ellipse at 50% 65%,#444 0%,#777 25%,#fff 60%)}
.pp-text{font-size:7.5px;color:#fff;line-height:14px;font-weight:600}
.copybar{left:72px;top:1157px;width:576px;height:31px;background:#fff;border-radius:0 0 5px 5px}
.copy{left:86px;top:1168px;font-size:6.5px;color:#222}
.legal{left:480px;top:1168px;font-size:6.5px;color:#222;display:flex;gap:8px}
</style>
</head>
<body>
<div class="canvas">

  <div class="abs topbar"></div>
  <nav class="abs toplinks"><a>Blog</a><a>Contact</a><a>Privacy</a><a>Terms</a></nav>
  <div class="abs signin">Sign In</div>
  <div class="abs field" style="left:408px;width:76px">Username</div>
  <div class="abs field" style="left:488px;width:76px">Password</div>
  <div class="abs go">Go</div>
  <div class="abs divider"></div>
  <a class="abs signup">Sign Up</a>

  <div class="abs logo-mark"></div>
  <div class="abs logo-name">Pellwick Trading Co</div>
  <div class="abs banner"><div class="banner-fill" role="img" aria-label="Close-up photo of a violin body and bridge"></div></div>

  <nav class="abs nav">
    <a class="active" style="width:44px">HOME</a>
    <a style="width:54px">ABOUT US</a>
    <a style="width:44px">NEWS</a>
    <a style="width:56px">PRODUCTS</a>
    <a style="width:76px">SALES NETWORK</a>
    <a style="width:55px">FEEDBACK</a>
    <a style="width:69px">RECRUITMENT</a>
  </nav>
  <div class="abs search">Search</div>
  <svg class="abs" style="left:620px;top:96px" width="10" height="10" viewBox="0 0 10 10"><circle cx="4" cy="4" r="3" fill="none" stroke="#c9392b" stroke-width="1.6"/><line x1="6.3" y1="6.3" x2="9" y2="9" stroke="#c9392b" stroke-width="1.8"/></svg>

  <div class="abs main"></div>

  <div class="abs hero" role="img" aria-label="Promotional photo of a black grand piano on a rose background"></div>
  <div class="abs hero-piano"></div>
  <div class="abs hero-kicker">limited edition</div>
  <div class="abs hero-title">Grand Piano</div>
  <div class="abs hero-sub">special offer this month</div>

  <div class="abs sec-title" style="left:90px;top:350px">LATEST ARRIVALS</div>
  <div class="abs sec-sub" style="left:90px;top:370px">Check our all latest products in this section.</div>
  <div class="abs rule" style="left:90px;top:388px;width:384px"></div>

  <div class="abs photo-guitar" style="left:90px;top:399px" role="img" aria-label="Electric guitar body photo"></div>
  <div class="abs photo-guitar" style="left:222px;top:399px" role="img" aria-label="Electric guitar body photo"></div>
  <div class="abs photo-guitar" style="left:354px;top:399px" role="img" aria-label="Electric guitar body photo"></div>
  <div class="abs photo-guitar" style="left:90px;top:533px" role="img" aria-label="Electric guitar body photo"></div>
  <div class="abs photo-guitar" style="left:222px;top:533px" role="img" aria-label="Electric guitar body photo"></div>
  <div class="abs photo-guitar" style="left:354px;top:533px" role="img" aria-label="Electric guitar body photo"></div>

  <div class="abs cap" style="left:90px;top:497px">Electric guitar Normal 4:3 800x600</div>
  <div class="abs cap" style="left:222px;top:497px">Electric guitar Normal 4:3 800x600</div>
  <div class="abs cap" style="left:354px;top:497px">Electric guitar Normal 4:3 800x600</div>
  <div class="abs cap" style="left:90px;top:631px">Electric guitar Normal 4:3 800x600</div>
  <div class="abs cap" style="left:222px;top:631px">Electric guitar Normal 4:3 800x600</div>
  <div class="abs cap" style="left:354px;top:631px">Electric guitar Normal 4:3 800x600</div>

  <div class="abs price" style="left:90px;top:510px">$300.00<span class="sep">|</span><span class="enquire"><svg width="8" height="6" viewBox="0 0 8 6"><rect x=".5" y=".5" width="7" height="5" fill="none" stroke="#555" stroke-width=".9"/><path d="M.5.5 4 3.5 7.5.5" fill="none" stroke="#555" stroke-width=".9"/></svg>Enquire</span></div>
  <div class="abs price" style="left:222px;top:510px">$300.00<span class="sep">|</span><span class="enquire"><svg width="8" height="6" viewBox="0 0 8 6"><rect x=".5" y=".5" width="7" height="5" fill="none" stroke="#555" stroke-width=".9"/><path d="M.5.5 4 3.5 7.5.5" fill="none" stroke="#555" stroke-width=".9"/></svg>Enquire</span></div>
  <div class="abs price" style="left:354px;top:510px">$300.00<span class="sep">|</span><span class="enquire"><svg width="8" height="6" viewBox="0 0 8 6"><rect x=".5" y=".5" width="7" height="5" fill="none" stroke="#555" stroke-width=".9"/><path d="M.5.5 4 3.5 7.5.5" fill="none" stroke="#555" stroke-width=".9"/></svg>Enquire</span></div>
  <div class="abs price" style="left:90px;top:644px">$300.00<span class="sep">|</span><span class="enquire"><svg width="8" height="6" viewBox="0 0 8 6"><rect x=".5" y=".5" width="7" height="5" fill="none" stroke="#555" stroke-width=".9"/><path d="M.5.5 4 3.5 7.5.5" fill="none" stroke="#555" stroke-width=".9"/></svg>Enquire</span></div>
  <div class="abs price" style="left:222px;top:644px">$300.00<span class="sep">|</span><span class="enquire"><svg width="8" height="6" viewBox="0 0 8 6"><rect x=".5" y=".5" width="7" height="5" fill="none" stroke="#555" stroke-width=".9"/><path d="M.5.5 4 3.5 7.5.5" fill="none" stroke="#555" stroke-width=".9"/></svg>Enquire</span></div>
  <div class="abs price" style="left:354px;top:644px">$300.00<span class="sep">|</span><span class="enquire"><svg width="8" height="6" viewBox="0 0 8 6"><rect x=".5" y=".5" width="7" height="5" fill="none" stroke="#555" stroke-width=".9"/><path d="M.5.5 4 3.5 7.5.5" fill="none" stroke="#555" stroke-width=".9"/></svg>Enquire</span></div>

  <div class="abs rule" style="left:90px;top:670px;width:384px"></div>
  <a class="abs more">more products</a>

  <div class="abs sec-title" style="left:90px;top:699px">OTHER PRODUCTS</div>
  <div class="abs sec-sub" style="left:90px;top:719px">Check our all latest products in this section</div>
  <div class="abs rule" style="left:90px;top:732px;width:384px"></div>

  <svg class="abs" style="left:90px;top:778px" width="16" height="16" viewBox="0 0 16 16"><circle cx="8" cy="8" r="8" fill="#111"/><path d="M9.5 4.5 6 8l3.5 3.5" fill="none" stroke="#fff" stroke-width="1.8"/></svg>
  <svg class="abs" style="left:614px;top:778px" width="16" height="16" viewBox="0 0 16 16"><circle cx="8" cy="8" r="8" fill="#111"/><path d="M6.5 4.5 10 8l-3.5 3.5" fill="none" stroke="#fff" stroke-width="1.8"/></svg>

  <div class="abs photo-violin" style="left:127px;top:745px" role="img" aria-label="Classical violin close-up photo"></div>
  <div class="abs photo-violin" style="left:247px;top:745px" role="img" aria-label="Classical violin close-up photo"></div>
  <div class="abs photo-violin" style="left:367px;top:745px" role="img" aria-label="Classical violin close-up photo"></div>
  <div class="abs photo-violin" style="left:487px;top:745px" role="img" aria-label="Classical violin close-up photo"></div>

  <div class="abs cap" style="left:127px;top:816px">Classical Violin C200 / S20</div>
  <div class="abs cap" style="left:247px;top:816px">Classical Violin C200 / S20</div>
  <div class="abs cap" style="left:367px;top:816px">Classical Violin C200 / S20</div>
  <div class="abs cap" style="left:487px;top:816px">Classical Violin C200 / S20</div>
  <div class="abs price" style="left:127px;top:827px">$25.00<span class="sep">|</span><a class="details">Details</a></div>
  <div class="abs price" style="left:247px;top:827px">$25.00<span class="sep">|</span><a class="details">Details</a></div>
  <div class="abs price" style="left:367px;top:827px">$25.00<span class="sep">|</span><a class="details">Details</a></div>
  <div class="abs price" style="left:487px;top:827px">$25.00<span class="sep">|</span><a class="details">Details</a></div>

  <div class="abs sec-title" style="left:491px;top:143px">BLOG UPDATES</div>
  <div class="abs rule" style="left:491px;top:164px;width:139px"></div>

  <div class="abs photo-keys" style="left:492px;top:174px" role="img" aria-label="Black and white photo of piano keys"></div>
  <div class="abs blog-title" style="left:491px;top:251px">This Will be The Title of Blog Goes Here</div>
  <div class="abs blog-text" style="left:491px;top:262px">Lorem ipsum dolor sit amet, consectetur adipisicing elit, sed do eiusmod tempor.</div>
  <div class="abs blog-date" style="left:491px;top:284px">23 July 2012 by <i>Marisa</i></div>

  <div class="abs photo-keys" style="left:492px;top:303px" role="img" aria-label="Black and white photo of piano keys"></div>
  <div class="abs blog-title" style="left:491px;top:380px">This Will be The Title of Blog Goes Here</div>
  <div class="abs blog-text" style="left:491px;top:391px">Lorem ipsum dolor sit amet, consectetur adipisicing elit, sed do eiusmod tempor.</div>
  <div class="abs blog-date" style="left:491px;top:413px">23 July 2012 by <i>Marisa</i></div>

  <div class="abs photo-keys" style="left:492px;top:432px" role="img" aria-label="Black and white photo of piano keys"></div>
  <div class="abs blog-title" style="left:491px;top:509px">This Will be The Title of Blog Goes Here</div>
  <div class="abs blog-text" style="left:491px;top:520px">Lorem ipsum dolor sit amet, consectetur adipisicing elit, sed do eiusmod tempor.</div>
  <div class="abs blog-date" style="left:491px;top:542px">23 July 2012 by <i>Marisa</i></div>

  <div class="abs sec-title" style="left:491px;top:563px">CHIRPNET UPDATES</div>
  <div class="abs tweet" style="left:491px;top:592px">@tunewire check the new products<br><span class="link">http://brf.ly/sun</span><br><span class="meta">About 1 hour ago via chirpfeed</span></div>
  <div class="abs tweet" style="left:491px;top:635px">@tunewire check the new products<br><span class="link">http://brf.ly/sun</span><br><span class="meta">About 1 hour ago via chirpfeed</span></div>
  <a class="abs" style="left:589px;top:676px;font-size:7px;color:#222;text-decoration:underline">More Tweets</a>

  <div class="abs redband"></div>
  <div class="abs lower"></div>
  <div class="abs about-title"><i>What</i> is Pellwick Trading Co ?</div>
  <p class="abs about-text" style="left:83px;top:901px;width:140px">Donec pellentesque, justo eget imperdiet viverra, lectus mi ornare arcu, non laoreet lacus lacus eleifend orci. Nam tincidunt vestibulum lacus nec pharetra. Nunc commodo aliquam lectus quis bibendum.</p>
  <div class="abs about-box" role="img" aria-label="Company team photo"></div>
  <p class="abs about-text" style="left:83px;top:954px;width:234px">Donec pellentesque, justo eget imperdiet viverra, lectus mi ornare arcu, non laoreet lacus lacus eleifend orci. Nam tincidunt vestibulum lacus nec pharetra. Nunc commodo aliquam lectus quis bibendum.</p>
  <div class="abs vline"></div>
  <div class="abs vdot"></div>

  <div class="abs news-title">Newsletter Subscription</div>
  <div class="abs news-input">you@yourcompany.com</div>
  <a class="abs news-btn">Sign-Up</a>

  <div class="abs follow"></div>
  <div class="abs follow-dot"></div>
  <a class="abs follow-btn">follow</a>
  <div class="abs rt-box">RT @playloud_: Check out our new special offers #newproduct<br>&nbsp;- <span class="link">http://www.pellwicktradingco.com</span> :D</div>

  <footer class="abs footer"></footer>
  <div class="abs fcol-title" style="left:90px;top:1026px">Popular Products</div>
  <div class="abs fcol-rule" style="left:90px;top:1044px;width:158px"></div>
  <div class="abs pp-thumb" style="left:90px;top:1054px"><div role="img" aria-label="Guitar product thumbnail"></div></div>
  <div class="abs pp-text" style="left:134px;top:1056px">Name of Product<br>$200</div>
  <div class="abs pp-thumb" style="left:90px;top:1096px"><div role="img" aria-label="Guitar product thumbnail"></div></div>
  <div class="abs pp-text" style="left:134px;top:1098px">Name of Product<br>$200</div>

  <div class="abs fcol-title" style="left:277px;top:1026px">Featured Clients</div>
  <div class="abs fcol-rule" style="left:277px;top:1044px;width:111px"></div>
  <ul class="abs flist" style="left:277px;top:1051px"><li>Name of Client</li><li>Name of Client</li><li>Name of Client</li><li>Name of Client</li><li>Name of Client</li><li>Name of Client</li></ul>

  <div class="abs fcol-title" style="left:416px;top:1026px">Partners</div>
  <div class="abs fcol-rule" style="left:416px;top:1044px;width:114px"></div>
  <ul class="abs flist" style="left:416px;top:1051px"><li>Name of Partner</li><li>Name of Partner</li><li>Name of Partner</li><li>Name of Partner</li><li>Name of Partner</li><li>Name of Partner</li></ul>

  <div class="abs fcol-title" style="left:558px;top:1026px">Pages</div>
  <div class="abs fcol-rule" style="left:558px;top:1044px;width:78px"></div>
  <ul class="abs flist" style="left:558px;top:1051px"><li>About Us</li><li>Contact Us</li><li>Recruitments</li><li>News</li><li>Feedback</li><li>Blogs</li></ul>

  <div class="abs copybar"></div>
  <div class="abs copy">Copyright 2012 | Pellwick Trading Co</div>
  <nav class="abs legal"><a>FAQ</a><span>/</span><a>Privacy Policy</a><span>/</span><a>API</a><span>/</span><a>Advertise</a></nav>

</div>
</body>
</html>
```